Business Card & Letterhead Design

We a financial advice company based in Australia. We provide advice to wealthy farmers.

We are changing our business name FROM Brightmere Financial TO Calderstone Wealth and we need a new letterhead and double sided business card design

Attached is designs from our previous branding (Brightmere Financial) as it includes all the details we require on the new Calderstone Wealth business cards and letterhead.

```html
<!DOCTYPE html>
<html lang="en">
<head>
<meta charset="utf-8">
<title>Calderstone Wealth Stationery</title>
<link href="https://fonts.googleapis.com/css2?family=Montserrat:wght@400;500&family=Cinzel:wght@400&display=swap" rel="stylesheet">
<style>
  :root {
    --bg: #e4e5e6;
    --paper: #ffffff;
    --slate: #5d6a71;
    --ink: #4a4a4a;
    --ink-soft: #5a5a5a;
    --faint: #f2f2f2;
  }
  * { box-sizing: border-box; margin: 0; padding: 0; }
  html, body { width: 1200px; height: 1200px; overflow: hidden; }
  body { background: var(--bg); font-family: "Montserrat", sans-serif; color: var(--ink); position: relative; }
  .sheet { position: absolute; background: var(--paper); box-shadow: 0 4px 14px rgba(0,0,0,.18); overflow: hidden; }

  /* Letterhead */
  .letterhead { left: 40px; top: 170px; width: 660px; height: 853px; }
  .brand { position: absolute; display: flex; flex-direction: column; align-items: center; }
  .brand-circle { border: 2px solid var(--ink); border-radius: 50%; }
  .brand-name { font-family: "Montserrat", sans-serif; font-weight: 500; color: var(--ink); letter-spacing: .06em; text-transform: uppercase; white-space: nowrap; }
  .brand-sub { font-weight: 400; color: var(--ink-soft); text-transform: uppercase; white-space: nowrap; }
  .letterhead .brand { left: 38px; top: 38px; width: 250px; }
  .letterhead .brand-circle { width: 66px; height: 66px; margin-bottom: 8px; }
  .letterhead .brand-name { font-size: 19px; }
  .letterhead .brand-sub { font-size: 8.5px; letter-spacing: .42em; margin-top: 2px; }

  .lh-contact { position: absolute; left: 420px; top: 38px; border-left: 1.5px solid var(--ink); padding-left: 20px; font-size: 10.8px; line-height: 1.25; color: var(--ink-soft); }
  .lh-contact p + p { margin-top: 3px; }
  .contact-line { display: flex; align-items: center; gap: 6px; white-space: nowrap; }
  .icon { width: 10px; height: 10px; fill: var(--ink-soft); flex: none; }

  .watermark { position: absolute; left: 256px; top: 452px; width: 520px; height: 520px; border: 20px solid var(--faint); border-radius: 50%; }

  .lh-footer { position: absolute; top: 740px; font-size: 10.8px; line-height: 1.25; color: var(--ink-soft); }
  .lh-footer.left { left: 39px; }
  .lh-footer.right { left: 425px; }
  .band { position: absolute; left: 0; bottom: 0; width: 100%; }
  .tagline { position: absolute; color: #fff; text-transform: uppercase; letter-spacing: .04em; white-space: nowrap; }
  .letterhead .tagline { right: 36px; bottom: 4px; font-size: 12.5px; }

  /* Business card front */
  .card { width: 440px; height: 251px; }
  .card-front { left: 740px; top: 240px; }
  .card-front .brand { right: 16px; top: 20px; width: 150px; }
  .card-front .brand-circle { width: 40px; height: 40px; margin-bottom: 5px; border-width: 1.5px; }
  .card-front .brand-name { font-size: 11.5px; }
  .card-front .brand-sub { font-size: 5px; letter-spacing: .4em; margin-top: 1px; }
  .card-front .watermark { left: 280px; top: 98px; width: 170px; height: 170px; border-width: 8px; }
  .holder { position: absolute; left: 16px; top: 88px; font-size: 9.5px; line-height: 1.38; color: var(--ink-soft); }
  .holder-name { font-family: "Cinzel", serif; font-size: 15px; color: var(--slate); line-height: 1; letter-spacing: .02em; }
  .card-list { position: absolute; font-size: 9.5px; line-height: 1.5; color: var(--ink-soft); }
  .card-list.contacts { left: 16px; top: 158px; }
  .card-list.address { left: 280px; top: 158px; }
  .card-list .icon { width: 8px; height: 8px; }
  .card-front .tagline { right: 16px; bottom: 2px; font-size: 8.4px; }

  /* Business card back */
  .card-back { left: 740px; top: 540px; background: var(--slate); }
  .card-back .brand { left: 0; right: 0; top: 78px; }
  .card-back .brand-circle { width: 64px; height: 64px; border-color: #c9cdd0; margin-bottom: 8px; }
  .card-back .brand-name { font-size: 18px; color: #d5d8da; }
  .card-back .brand-sub { font-size: 7.6px; letter-spacing: .4em; color: #c9cdd0; margin-top: 2px; }
  .card-back .tagline { left: 0; right: 0; text-align: center; bottom: 16px; font-size: 8.8px; }
</style>
</head>
<body>

<svg width="0" height="0" style="position:absolute" aria-hidden="true">
  <symbol id="i-phone" viewBox="0 0 10 10"><path d="M1 3.2C1 2 2.4 1.5 5 1.5S9 2 9 3.2V4H7V3.2H3V4H1Z"/><path d="M2.5 4.5h5l1 4h-7z"/></symbol>
  <symbol id="i-fax" viewBox="0 0 10 10"><rect x="2.5" y="1" width="5" height="2.5"/><rect x="1" y="3.8" width="8" height="3.5" rx=".6"/><rect x="2.5" y="6.5" width="5" height="2.5"/></symbol>
  <symbol id="i-mail" viewBox="0 0 10 10"><path d="M1 2h8v6H1z M1.6 2.6 5 5.4 8.4 2.6" stroke="#fff" stroke-width=".7"/></symbol>
  <symbol id="i-web" viewBox="0 0 10 10"><circle cx="5" cy="5" r="4"/><path d="M3 3.5l2 .5 .5 2-1 1.5-1-1.5zM6.5 2.5l1 1-1 .5z" fill="#fff"/></symbol>
  <symbol id="i-mobile" viewBox="0 0 10 10"><path d="M3 .5h4a.8.8 0 0 1 .8.8v7.4a.8.8 0 0 1-.8.8H3a.8.8 0 0 1-.8-.8V1.3A.8.8 0 0 1 3 .5zm.2 1.2v5.8h3.6V1.7z"/></symbol>
</svg>

<!-- Letterhead -->
<section class="sheet letterhead">
  <div class="watermark" aria-hidden="true"></div>

  <div class="brand">
    <div class="brand-circle"></div>
    <div class="brand-name">Calderstone Wealth</div>
    <div class="brand-sub">Strategic Financial Advice</div>
  </div>

  <div class="lh-contact">
    <p>Suite 4A, 18 Wexley St<br>Riverside QLD 4170</p>
    <p>PO Box 5120<br>Eastvale QLD 4170</p>
    <p class="contact-line"><svg class="icon"><use href="#i-phone"/></svg>(07) 3000 1842</p>
    <p class="contact-line"><svg class="icon"><use href="#i-fax"/></svg>(07) 3000 1843</p>
    <p class="contact-line"><svg class="icon"><use href="#i-mail"/></svg>tom@brightmerefinancial.com.au</p>
    <p class="contact-line"><svg class="icon"><use href="#i-web"/></svg>www.brightmerefinancial.com.au</p>
  </div>

  <div class="lh-footer left">
    Arlow Holdings Pty Ltd<br>
    ATF The Fernlea Investment<br>
    Trust T/AS Brightmere Financial<br>
    ABN: 00 000 000 001<br>
    Corporate Authorised<br>
    Representative of Meridian<br>
    Advice Partners Limited
  </div>
  <div class="lh-footer right">
    Meridian Advice Partners Limited<br>
    ABN 00 000 000 002<br>
    Australian Financial Services Licence<br>
    Licence Number 000 111<br>
    Principal Address: 120 Harbour Rd<br>
    PO Box 1000 Melbourne VIC 3000
  </div>

  <svg class="band" width="660" height="26" viewBox="0 0 660 26" aria-hidden="true">
    <polygon points="0,13 378,13 370,26 0,26" fill="var(--slate)"/>
    <polygon points="396,0 660,0 660,26 380,26" fill="var(--slate)"/>
  </svg>
  <div class="tagline">'Wealth Built to Last'</div>
</section>

<!-- Business card: front -->
<section class="sheet card card-front">
  <div class="watermark" aria-hidden="true"></div>

  <div class="brand">
    <div class="brand-circle"></div>
    <div class="brand-name">Calderstone Wealth</div>
    <div class="brand-sub">Strategic Financial Advice</div>
  </div>

  <div class="holder">
    <div class="holder-name">TOM HARDIE</div>
    B.Com. Adv Dip Fin Plan<br>
    Managing Director<br>
    Authorised Representative
  </div>

  <div class="card-list contacts">
    <p class="contact-line"><svg class="icon"><use href="#i-mobile"/></svg>0400 123 456</p>
    <p class="contact-line"><svg class="icon"><use href="#i-phone"/></svg>(07) 3000 1842</p>
    <p class="contact-line"><svg class="icon"><use href="#i-fax"/></svg>(07) 3000 1843</p>
    <p class="contact-line"><svg class="icon"><use href="#i-mail"/></svg>tom@brightmerefinancial.com.au</p>
    <p class="contact-line"><svg class="icon"><use href="#i-web"/></svg>www.brightmerefinancial.com.au</p>
  </div>

  <div class="card-list address">
    PO Box 5120<br>
    Eastvale QLD 4170<br><br>
    Suite 4A, 18 Wexley St<br>
    Riverside QLD 4170
  </div>

  <svg class="band" width="440" height="17" viewBox="0 0 440 17" aria-hidden="true">
    <polygon points="0,9 258,9 253,17 0,17" fill="var(--slate)"/>
    <polygon points="272,0 440,0 440,17 262,17" fill="var(--slate)"/>
  </svg>
  <div class="tagline">'Wealth Built to Last'</div>
</section>

<!-- Business card: back -->
<section class="sheet card card-back">
  <div class="brand">
    <div class="brand-circle"></div>
    <div class="brand-name">Calderstone Wealth</div>
    <div class="brand-sub">Strategic Financial Advice</div>
  </div>
  <div class="tagline">'Wealth Built to Last'</div>
</section>

</body>
</html>
```